Skin Care Company Branding/Design for Product Packaging

Hello,

We need help with designing box/container graphics for our skin care company, Velvora Beauty Co.

I've attached two boxes from our competitors. One is a pimple patch box and one is a dry face towel box.

We want our brand to appear professional, modern, and clean.

We want the design and colors for all of our products to go together.

Please do your design work on the images we provided. You can remove any content from the other brands. If you have major issues with these images please use something very similar.

The product details our products and our competitors will be almost identical but our company name and the colors will be different.

Please take your time on this. We have already done several products on this page and will have many more to come. If we really like your work we could select you to work with us.

The box dimensions for the face towels are: 6.25 x 5.25 x 4.75. If you are having trouble seeing the image please use the Dewmoss Face Lab 50 count image off of Trovamart.

The box dimensions or the acne patches are: 5.5 x 3.25 x 0.75. If you are having trouble seeing the image please us the Nimbo Quell Dot (red and white box) on Trovamart.

Our boxes for these two products are a carton type paper.

We are open to colors but it needs to look very clean, modern and eye catching. We are open to any color combination but particularly like the idea of an color combination of white and another color like Dulmira or the Nimbo Quell Dot box.

Target Market(s)

Towels will be primarily female. Acne patches will be both male and female but primarily female.

Industry/Entity Type

Health & Beauty Products

Requirements
Must have
• Design work on the boxes in the images I provided.

```html
<!DOCTYPE html>
<html lang="en">
<head>
<meta charset="utf-8">
<title>Velvora Beauty Co. – Face Cloth Carton Dieline</title>
<link rel="stylesheet" href="https://fonts.googleapis.com/css2?family=Source+Sans+3:wght@400;600&display=swap">
<style>
  :root {
    --paper: #ffffff;
    --ink: #111111;
    --cut-line: #1a1a1a;
    --silver-light: #e6e8eb;
    --silver-mid: #cfd3d8;
    --navy: #2b2d92;
    --navy-light: #3f5fb0;
    --brand-grey: #4a4d53;
    --on-navy: #f4f6fb;
  }
  html, body {
    margin: 0;
    padding: 0;
    width: 1200px;
    height: 571px;
    overflow: hidden;
    background: var(--paper);
  }
  .dieline-sheet { display: block; width: 1200px; height: 571px; }
  .sheet-title { font-family: "Source Sans 3", sans-serif; fill: var(--ink); }
  .brand-name { font-family: "Source Sans 3", sans-serif; font-weight: 400; font-size: 28px; letter-spacing: 1px; fill: var(--brand-grey); }
  .count-line { font-family: "Source Sans 3", sans-serif; font-weight: 600; font-size: 17px; fill: var(--on-navy); }
  .product-line { font-family: "Source Sans 3", sans-serif; font-weight: 400; font-size: 17px; fill: var(--on-navy); }
  .claims-strip { font-family: "Source Sans 3", sans-serif; font-size: 9px; fill: var(--on-navy); }
  .panel-heading { font-family: "Source Sans 3", sans-serif; font-weight: 600; font-size: 12px; fill: var(--ink); }
  .panel-copy { font-family: "Source Sans 3", sans-serif; font-size: 8px; fill: #333; }
  .print-info { font-family: "Source Sans 3", sans-serif; font-size: 9px; fill: var(--ink); }
  .cut { fill: none; stroke: var(--cut-line); stroke-width: 1.6; }
  .fold { fill: none; stroke: var(--cut-line); stroke-width: 1.6; stroke-dasharray: 4 3; }
  .flap-blank { fill: var(--paper); stroke: var(--cut-line); stroke-width: 1.6; }
</style>
</head>
<body>
<svg class="dieline-sheet" viewBox="0 0 2560 1218" xmlns="http://www.w3.org/2000/svg" aria-label="Velvora Beauty Co. face cloth carton, flat dieline">
  <defs>
    <linearGradient id="soft-silver" x1="0" y1="0" x2="1" y2="0">
      <stop offset="0" stop-color="var(--silver-mid)"/>
      <stop offset="1" stop-color="var(--silver-light)"/>
    </linearGradient>
    <linearGradient id="navy-band" x1="0" y1="0" x2="1" y2="0">
      <stop offset="0" stop-color="var(--navy)"/>
      <stop offset="1" stop-color="var(--navy-light)"/>
    </linearGradient>
  </defs>

  <g class="sheet-heading">
    <text class="sheet-title" x="46" y="95" font-size="64">Velvora Beauty Co.</text>
    <text class="sheet-title" x="52" y="133" font-size="28">The box dimensions for the face towels</text>
    <text class="sheet-title" x="52" y="178" font-size="48">6.25 x 5.25 x 4.75.</text>
  </g>

  <g class="dust-flaps">
    <polygon class="flap-blank" points="720,641 747,591 955,591 955,641"/>
    <polygon class="flap-blank" points="1263,641 1263,591 1470,591 1497,641"/>
    <polygon class="flap-blank" points="1497,641 1535,672 1535,900 1497,900"/>
  </g>

  <g class="bottom-flaps">
    <polygon class="flap-blank" points="413,900 516,998 516,1047 616,1047 616,998 720,900"/>
    <polygon class="flap-blank" points="720,900 720,1077 835,1077 835,1027 955,900"/>
    <path class="flap-blank" d="M955,900 V1006 H1050 V990 Q1108,970 1167,990 V1006 H1263 V900 Z"/>
    <polygon class="flap-blank" points="1263,900 1383,1027 1383,1077 1497,1077 1497,900"/>
    <g class="print-info" transform="rotate(180 1215 940)">
      <text x="1190" y="925">Expiry Date:</text>
      <text x="1190" y="937">Mfg Date:</text>
      <text x="1190" y="949">Batch No:</text>
      <text x="1190" y="961">Regn No.</text>
    </g>
  </g>

  <g class="back-insert">
    <polygon points="104,641 148,660 148,757 262,805 368,757 368,660 413,641 413,900 104,900" fill="url(#soft-silver)" class="cut"/>
  </g>

  <g class="side-panel-left">
    <rect x="413" y="641" width="307" height="259" fill="url(#soft-silver)"/>
    <rect x="413" y="790" width="307" height="110" fill="url(#navy-band)"/>
    <polyline class="fold" points="413,641 458,660 458,760 570,820 676,760 676,660 720,641"/>
    <circle cx="473" cy="778" r="20" fill="var(--paper)" class="cut"/>
    <text class="count-line" x="705" y="840" text-anchor="end">50 COUNT</text>
    <text class="product-line" x="705" y="860" text-anchor="end">PURE CLOTHS XL</text>
    <text class="claims-strip" x="566" y="893" text-anchor="middle">EXTRA SOFT | PLANT-BASED FIBER | DERM TESTED | VEGAN</text>
  </g>

  <g class="info-panel">
    <rect x="720" y="641" width="235" height="259" fill="url(#soft-silver)"/>
    <text class="panel-heading" x="739" y="663">PURE CLOTHS</text>
    <g class="panel-copy">
      <rect x="731" y="672" width="5" height="5"/><text x="739" y="678">50 dermatologist tested, plant-based face</text>
      <text x="739" y="692">cloths.</text>
      <rect x="731" y="700" width="5" height="5"/><text x="739" y="706">Shown to help achieve visibly clearer skin,</text>
      <text x="739" y="720">less irritation, and to reduce the look of</text>
      <text x="739" y="734">redness.</text>
      <rect x="731" y="742" width="5" height="5"/><text x="739" y="748">A fresh, clean cloth for drying your face.</text>
      <rect x="731" y="756" width="5" height="5"/><text x="739" y="762">Cellulose fiber designed to support overall</text>
      <text x="739" y="776">skin health and skin barrier function.</text>
      <rect x="731" y="784" width="5" height="5"/><text x="739" y="790">100% vegan &amp; cruelty free.</text>
    </g>
  </g>

  <g class="front-panel">
    <rect x="955" y="641" width="308" height="259" fill="url(#soft-silver)"/>
    <rect x="955" y="790" width="308" height="110" fill="url(#navy-band)"/>
    <text class="brand-name" x="1109" y="722" text-anchor="middle">VELVORA BEAUTY CO.</text>
    <text class="count-line" x="1249" y="840" text-anchor="end">50 COUNT</text>
    <text class="product-line" x="1249" y="860" text-anchor="end">PURE CLOTHS XL</text>
    <text class="claims-strip" x="1109" y="893" text-anchor="middle">EXTRA SOFT | PLANT-BASED FIBER | DERM TESTED | VEGAN</text>
  </g>

  <g class="side-panel-right">
    <rect x="1263" y="641" width="234" height="259" fill="url(#soft-silver)"/>
    <text class="panel-heading" x="1277" y="708">Daily uses for your Pure Cloths</text>
    <g class="panel-copy">
      <text x="1300" y="724">Dry your face</text>
      <text x="1300" y="734">Pair with a cleanser or makeup remover</text>
      <text x="1300" y="744">Wet and remove face masks</text>
      <text x="1300" y="754">Clean your skincare &amp; makeup tools</text>
    </g>
  </g>

  <g class="top-panel">
    <rect x="955" y="407" width="308" height="234" fill="url(#soft-silver)"/>
    <rect x="955" y="407" width="308" height="110" fill="url(#navy-band)"/>
    <g transform="rotate(180 1109 524)">
      <text class="brand-name" x="1109" y="523" text-anchor="middle">VELVORA BEAUTY CO.</text>
      <text class="count-line" x="1249" y="581" text-anchor="end">50 COUNT</text>
      <text class="product-line" x="1249" y="601" text-anchor="end">PURE CLOTHS XL</text>
      <text class="claims-strip" x="1109" y="634" text-anchor="middle">EXTRA SOFT | PLANT-BASED FIBER | DERM TESTED | VEGAN</text>
    </g>
  </g>

  <g class="tuck-flap">
    <polygon points="1000,280 1105,228 1218,280 1218,385 1263,407 955,407 1000,385" fill="url(#soft-silver)"/>
    <polyline class="fold" points="955,407 1000,385 1000,280 1105,228 1218,280 1218,385 1263,407"/>
    <g transform="rotate(180 1109 330)">
      <text class="brand-name" x="1109" y="330" text-anchor="middle">VELVORA BEAUTY CO.</text>
    </g>
  </g>

  <g class="fold-lines">
    <line class="cut" x1="413" y1="641" x2="413" y2="900"/>
    <line class="cut" x1="720" y1="641" x2="720" y2="900"/>
    <line class="cut" x1="955" y1="407" x2="955" y2="900"/>
    <line class="cut" x1="1263" y1="407" x2="1263" y2="900"/>
    <line class="cut" x1="1497" y1="641" x2="1497" y2="900"/>
    <line class="cut" x1="720" y1="641" x2="1497" y2="641"/>
    <line class="cut" x1="104" y1="900" x2="1535" y2="900"/>
  </g>
</svg>
</body>
</html>
```